National Training and assessment company needs a website

Create a 4 page website, simple but professional, the company provides training services to industry, resumes'/ CVs, personnel skill assessment, workplace skills profiling and develops manufactures and supplies training equipment for electrical/engineering training, Company title is Toren K Pty Ltd and also trades under BRW & Associates. letterheads etc all are done using dark green
Reason: Due to work commitments will be interstate from the 26/02 til 05/03/14
Target Market(s)
The market is broad covering the general public, secondary colleges and corporate sector
Industry/Entity Type
Training
Look and feel

```html
<!DOCTYPE html>
<html lang="en">
<head>
<meta charset="utf-8">
<title>Toren K Pty Ltd</title>
<link href="https://fonts.googleapis.com/css2?family=Roboto+Condensed:wght@300;400;700&family=Roboto:wght@400;700&family=Dancing+Script:wght@500&display=swap" rel="stylesheet">
<style>
:root{
  --green:#0a870a;
  --green-dark:#066a06;
  --yellow:#ffc412;
  --yellow-dark:#e9a400;
  --ink:#222;
  --grey:#8b8b8b;
  --light:#e6e6e6;
  --band:#262626;
  --white:#fff;
}
*{margin:0;padding:0;box-sizing:border-box}
html,body{width:794px;height:1200px;overflow:hidden;background:var(--white)}
body{position:relative;font-family:"Roboto",Arial,sans-serif;color:var(--ink)}
.abs{position:absolute}

/* header */
.wordmark{left:157px;top:19px;display:flex;align-items:center;gap:7px;font:400 17px/1 "Roboto Condensed",sans-serif;color:var(--green)}
.wordmark i{width:13px;height:13px;background:var(--green);display:block}
.follow{left:470px;top:15px;font:700 8px/1 "Roboto Condensed",sans-serif;color:var(--green)}
.follow-dots{left:516px;top:15px;display:flex;gap:7px}
.dot{width:8px;height:8px;border-radius:50%;background:#444}
.phone{left:404px;top:40px;font:italic 10px/1 Georgia,serif;color:#555;display:flex;gap:3px;align-items:center}
.search{left:477px;top:37px;width:166px;height:16px;border:1px solid #ddd;font-size:7px;color:#bbb;padding:4px 0 0 70px}
.search svg{position:absolute;right:5px;top:3px}

/* nav */
.nav{left:0;top:59px;width:794px;height:30px;background:var(--green)}
.nav ul{position:absolute;left:163px;top:11px;display:flex;gap:14px;list-style:none;font:700 10px/1 "Roboto Condensed",sans-serif;color:var(--white)}
.btn-yellow{background:var(--yellow);color:#333;font:700 9px/1 "Roboto Condensed",sans-serif;display:flex;align-items:center;justify-content:center;border-radius:2px;box-shadow:inset 0 -2px 0 var(--yellow-dark)}
.nav-cta{left:509px;top:63px;width:135px;height:22px}

/* hero */
.hero-photo{left:0;top:89px;width:794px;height:298px;background:linear-gradient(90deg,#b8b5b0 0%,#dedcd8 25%,#3a3d44 40%,#eceae6 55%,#f2f1ef 75%,#c9c3bd 100%)}
.hero-title{left:441px;top:192px;font:400 34px/0.9 "Roboto Condensed",sans-serif;color:var(--green)}
.hero-text{left:441px;top:258px;width:175px;font:400 7px/1.5 "Roboto",sans-serif;color:#888}
.arrow{width:25px;height:25px;border-radius:50%;border:2px solid rgba(120,120,120,.6)}
.hero-band{left:152px;top:329px;width:497px;height:58px;background:rgba(40,40,40,.85)}
.hero-band h2{position:absolute;left:13px;top:19px;font:700 11px/1 "Roboto Condensed",sans-serif;color:var(--white)}
.hero-band p{position:absolute;left:13px;top:33px;font-size:7px;color:#ddd}
.hero-band .btn-yellow{position:absolute;left:353px;top:15px;width:135px;height:23px;font-size:9px}

/* features */
.features{left:0;top:387px;width:794px;height:183px;background:var(--green)}
.feature{position:absolute;top:6px;width:100px;color:var(--white)}
.feature .icon{width:24px;height:24px;border-radius:50%;margin-left:20px;background:rgba(255,255,255,.35)}
.feature h3{margin-top:14px;font:300 13px/1.05 "Roboto Condensed",sans-serif;text-transform:uppercase}
.feature p{position:absolute;top:82px;font-size:7px;line-height:1.5}
.more{position:absolute;top:133px;width:52px;height:14px;background:var(--yellow);font-size:6px;color:var(--white);padding:4px 5px}
.signup-input{position:absolute;left:0;top:84px;width:132px;height:15px;background:var(--white);font-size:6px;color:#bbb;padding:4px}
.signup-btn{position:absolute;left:1px;top:109px;width:51px;height:14px;background:#111;color:var(--white);font-size:6px;text-align:center;padding-top:4px}

/* services */
.section-title{left:0;width:794px;text-align:center;font:700 14px/1 "Roboto Condensed",sans-serif;color:#8a8a8a}
.svc-photo{width:111px;height:74px;border:3px solid #eee}
.svc h3{font:300 12px/1.08 "Roboto Condensed",sans-serif;color:var(--green);text-transform:uppercase}
.svc p{margin-top:5px;width:122px;font-size:7px;line-height:1.5;color:#999}
.svc .link{margin-top:2px;font-size:6.5px;color:#333}
.svc .link b{color:var(--yellow-dark)}
.rule{left:152px;top:816px;width:497px;height:1px;background:var(--light)}

/* speakers */
.speaker-photo{width:36px;height:36px;border:2px solid #eee;background:linear-gradient(#d8b89e,#a8826a)}
.speaker h4{font:300 12px/1 "Roboto Condensed",sans-serif;color:var(--green);text-transform:uppercase}
.speaker .role{margin-top:3px;font:400 7.5px/1.3 "Roboto Condensed",sans-serif;color:#222}
.speaker .role span{color:#999;display:block}
.speaker-note{font-size:7px;line-height:1.5;color:#999;width:105px}

/* quote */
.quote{left:152px;top:918px;width:497px;height:61px;background:linear-gradient(var(--band),#111)}
.quote p{position:absolute;left:25px;top:13px;font:500 13px/1.35 "Dancing Script",cursive;color:var(--white)}
.quote .by{position:absolute;right:48px;top:24px;text-align:right;font-size:7px;line-height:1.5;color:#eee}
.quote .avatar{position:absolute;right:13px;top:17px;width:32px;height:28px;border:2px solid #ddd;background:linear-gradient(#c9a68c,#8f6c56)}

/* footer */
.footer{left:152px;top:988px;width:497px;height:179px;background:var(--green);color:var(--white)}
.footer h5{position:absolute;top:15px;font:700 11px/1 "Roboto Condensed",sans-serif}
.contact{position:absolute;left:6px;top:31px;font-size:7.5px;line-height:1.4}
.contact .big{font-size:12px}
.feed{position:absolute;left:167px;top:35px;width:135px;font-size:5.5px;line-height:1.8}
.feed b{font-size:6px}
.form{position:absolute;left:326px;top:32px;width:153px}
.form div{background:var(--white);height:15px;margin-bottom:9px;font-size:7px;color:#aaa;padding:3px 5px}
.form .msg{height:42px}
.form .send{width:58px;height:17px;background:var(--green-dark);border:1px solid #4db84d;color:var(--white);font:italic 700 8px/1 "Roboto",sans-serif;text-align:center;padding-top:4px;margin-top:-1px}
.copy{left:158px;top:1177px;font-size:6px;color:#444}
.foot-dots{left:446px;top:1178px;display:flex;gap:7px}
.foot-dots .dot{width:7px;height:7px;background:#333}
</style>
</head>
<body>

<header>
  <div class="abs wordmark"><i></i>Toren K Pty Ltd · BRW &amp; Associates</div>
  <div class="abs follow">FOLLOW US</div>
  <div class="abs follow-dots"><i class="dot"></i><i class="dot"></i><i class="dot"></i><i class="dot"></i><i class="dot"></i><i class="dot"></i><i class="dot"></i><i class="dot"></i><i class="dot"></i></div>
  <div class="abs phone">
    <svg width="8" height="9" viewBox="0 0 8 9"><path d="M2 0 L3 2.5 L2 3.5 Q3 6 5 7 L6 6 L8 7.5 L7 9 Q1 8 0 1 Z" fill="#444"/></svg>
    0400 123 456
  </div>
  <div class="abs search">Search
    <svg width="9" height="9" viewBox="0 0 9 9"><circle cx="3.7" cy="3.7" r="2.8" fill="none" stroke="#222" stroke-width="1.3"/><path d="M5.8 5.8 L8.5 8.5" stroke="#222" stroke-width="1.5"/></svg>
  </div>
</header>

<nav class="abs nav">
  <ul><li>HOME</li><li>ABOUT US</li><li>SERVICES</li><li>SUCCESS STORIES</li><li>CONTACTS</li></ul>
</nav>
<div class="abs btn-yellow nav-cta">REGISTRATION &nbsp;NOW!</div>

<section>
  <div class="abs hero-photo" role="img" aria-label="Photo of a presenter in a suit pointing to a growth chart on a whiteboard while seated colleagues watch"></div>
  <h1 class="abs hero-title">DEVELOP YOUR<br>PERSONALITY</h1>
  <p class="abs hero-text">Praesent vestibulum molestie lacus. Aenean nonummy hendrerit mauris. Phasellus porta. Fusce suscipit varius.</p>
  <div class="abs arrow" style="left:8px;top:238px"></div>
  <div class="abs arrow" style="left:764px;top:238px;border-color:rgba(10,135,10,.7)"></div>
  <div class="abs hero-band">
    <h2>DO NOT MISS YOU CHANCE TO GET THE BEST PLACE</h2>
    <p>Lorem ipsum dolor sit amet, consectetuer adipiscing elit.</p>
    <div class="btn-yellow">REGISTRATION &nbsp;NOW!</div>
  </div>
</section>

<section class="abs features">
  <div class="feature" style="left:162px">
    <div class="icon" role="img" aria-label="Speech bubbles icon"></div>
    <h3>How we can<br>help you?</h3>
    <p>Vestibulum molestie lacus. Aenean nonummy hendrerit mauris. Phasellus porta. Fusce suscipit varius mi.</p>
    <div class="more">Read More »</div>
  </div>
  <div class="feature" style="left:274px;width:110px">
    <div class="icon" role="img" aria-label="Pen nib icon"></div>
    <h3>Company provides training services to industry</h3>
    <p>Praesent vestibulum molestie lacus. Aenean nonummy hendrerit mauris. Phasellus porta. Fusce suscipit varius.</p>
    <div class="more">Read More »</div>
  </div>
  <div class="feature" style="left:398px">
    <div class="icon" role="img" aria-label="Group of people icon"></div>
    <h3>Best training<br>are here</h3>
    <p>Aenean nonummy hendrerit mauris. Phasellus porta. Fusce suscipit varius mi. Cum sociis natoque penatibus.</p>
    <div class="more">Read More »</div>
  </div>
  <div class="feature" style="left:510px;width:135px">
    <div class="icon" role="img" aria-label="Email envelope icon"></div>
    <h3>Sign up here</h3>
    <div class="signup-input">Enter your Email here</div>
    <div class="signup-btn">Submit</div>
  </div>
</section>

<h2 class="abs section-title" style="top:582px">THE COMPANY PROVIDES &nbsp;OUR TRAINING SERVICES TO INDUSTRY</h2>

<div class="abs svc-photo" style="left:158px;top:618px;background:linear-gradient(135deg,#e9e2d6,#a8917a)" role="img" aria-label="Photo of colleagues around a meeting table"></div>
<div class="abs svc" style="left:276px;top:620px">
  <h3>Employer workplace<br>skills profiling</h3>
  <p>Vestibulum molestie lacus. Aenean nonummy hendrerit mauris. Phasellus porta.</p>
  <div class="link">Read More <b>»</b></div>
</div>
<div class="abs svc-photo" style="left:406px;top:618px;background:linear-gradient(135deg,#c8a77a,#5a4030)" role="img" aria-label="Photo of a woman working at a laptop"></div>
<div class="abs svc" style="left:523px;top:620px">
  <h3>Employee skills<br>profiling</h3>
  <p>Vestibulum molestie lacus. Aenean nonummy hendrerit mauris. Phasellus porta.</p>
  <div class="link">Read More <b>»</b></div>
</div>
<div class="abs svc-photo" style="left:158px;top:731px;background:linear-gradient(135deg,#f0efec,#777068)" role="img" aria-label="Photo of a workplace training session around a table"></div>
<div class="abs svc" style="left:276px;top:730px">
  <h3>Workplace training<br>and assessment</h3>
  <p>Vestibulum molestie lacus. Aenean nonummy hendrerit mauris. Phasellus porta.</p>
  <div class="link">Read More <b>»</b></div>
</div>
<div class="abs svc-photo" style="left:406px;top:731px;background:linear-gradient(135deg,#e07a3a,#c8b0a0 55%,#f2f2f2)" role="img" aria-label="Photo of smiling students holding notebooks"></div>
<div class="abs svc" style="left:525px;top:730px">
  <h3>Resume and curricula<br>vita compilation</h3>
  <p>Vestibulum molestie lacus. Aenean nonummy hendrerit mauris. Phasellus porta.</p>
  <div class="link">Read More <b>»</b></div>
</div>

<div class="abs rule"></div>
<h2 class="abs section-title" style="top:822px">OUR WORLD CLASS SPEAKERS</h2>

<div class="abs speaker-photo" style="left:164px;top:849px" role="img" aria-label="Portrait photo of speaker"></div>
<div class="abs speaker" style="left:208px;top:852px"><h4>Clara Venn</h4><div class="role">Senior Developer,<span>Northgate Capital</span></div></div>
<div class="abs speaker-note" style="left:164px;top:891px">Who has 11 items, including the newest from the Kites.</div>

<div class="abs speaker-photo" style="left:281px;top:849px" role="img" aria-label="Portrait photo of speaker"></div>
<div class="abs speaker" style="left:324px;top:852px"><h4>Lena Hart</h4><div class="role">Marketing Director,<span>Brightline Media</span></div></div>
<div class="abs speaker-note" style="left:280px;top:891px">Datured author is PaperKite, cluding.</div>

<div class="abs speaker-photo" style="left:406px;top:849px" role="img" aria-label="Portrait photo of speaker"></div>
<div class="abs speaker" style="left:449px;top:852px"><h4>Owen Tate</h4><div class="role">Story teller,<span>Kestrel Works</span></div></div>
<div class="abs speaker-note" style="left:406px;top:891px">This week's featured author .</div>

<div class="abs speaker-photo" style="left:531px;top:849px" role="img" aria-label="Portrait photo of speaker"></div>
<div class="abs speaker" style="left:575px;top:852px"><h4>Reid Cole</h4><div class="role">Senior SEO expert,<span>Kestrel Works</span></div></div>
<div class="abs speaker-note" style="left:531px;top:891px">This week's featured author .</div>

<div class="abs quote">
  <p>“This Conference is my passion for already 20 years!<br>And I’m proud to be a speaker of Summit”</p>
  <div class="by">Paul Whitcombe<br>SUMMIT 2018 CEO Cheef Officer</div>
  <div class="avatar" role="img" aria-label="Portrait photo of the quoted speaker"></div>
</div>

<footer class="abs footer">
  <h5 style="left:6px">CONTACT INFORMATION</h5>
  <div class="contact">
    Toren K Pty Ltd<br>P.O. Box 2210<br>Elmwood Ridge<br>Victoria-3000<br>
    <div style="margin-top:14px">Phone: <span class="big">0400 123 456</span></div>
    <div>Fax: &nbsp;&nbsp;<span class="big" style="font-size:11px">(03)95550187</span></div>
  </div>
  <h5 style="left:167px">NEWS FEED</h5>
  <div class="feed">
    <b>@TKnews</b> it seems you have an old version of the theme. Update the theme to its latest version and it should be ok. Cheers!<br><b>6 days ago</b>
    <div style="margin-top:12px"><b>@TKnews</b> Hey, the demo page is also on WP 3.8, so no problems<br><b>6 days ago</b></div>
  </div>
  <h5 style="left:326px">LEAVE US A MESSAGE</h5>
  <div class="form">
    <div>Name</div><div>E-mail</div><div style="margin-top:-3px">Subject</div><div class="msg">Message</div>
    <div class="send">SUBMIT</div>
  </div>
</footer>

<div class="abs copy">Copyright © 2014 - Toren K Pty Ltd</div>
<div class="abs foot-dots"><i class="dot"></i><i class="dot"></i><i class="dot"></i><i class="dot"></i><i class="dot"></i><i class="dot"></i><i class="dot"></i><i class="dot"></i><i class="dot"></i><i class="dot"></i><i class="dot"></i><i class="dot"></i><i class="dot"></i></div>

</body>
</html>
```